Theatrical Illusion Show poster

For a new proffesional magic show that will be made in a theater in Switzerland we need a design of a poster. This posters will be out all over the city. It will be printed in A3.
The show is all about shadows and is not a traditional magic show but a contemporary fusion of magic, mentalism, storytelling and shadowplay. No cliche glitter and glamour las vegas style, but meaningfull theaterical piece. It should be clean proffesional. Not have a feel its AI generated..
Text should be like in the example poster. The design can also be exactly like the example we Included here. We like the design to be simpel. For example a white background, a spotlight from the front, and two shadows that act diffrent than the magician. Butterflys are important in the story and should be included.
Foto of the artist on the poster is not obligatory.
Text :
Die leise Lampe
Lorenz Habicht
Fesselndes Zauber-Theater
27. bis 30. Mai 2026 - 20:00 - Dachstube St. Gallen
Tickets: www.dachstubbe.ch - 071 84 16 72

Target Market(s)

Familie audience - Cultural intrested people

Industry/Entity Type

Theater, art, entertainment

Requirements
Must have
• The shadows in the background should do something diffrent. Butterflys in shadow. Name of the show, artist name and 5 cm space down for date, time, place etc.
Should not have
• It should not be very colourfull or over the top cliche magician poster.

```html
<!DOCTYPE html>
<html lang="de">
<head>
<meta charset="utf-8">
<title>Die leise Lampe – Lorenz Habicht</title>
<link rel="stylesheet" href="https://fonts.googleapis.com/css2?family=Bodoni+Moda:opsz,wght@6..96,400;6..96,500&family=Barlow+Semi+Condensed:wght@400&display=swap">
<style>
  :root {
    --backdrop: #e6e6e6;
    --paper: #ffffff;
    --ink: #0b0b0b;
    --mist: #d8d8d8;
    --smoke: #8a8a8a;
    --shadow-grey: #7e7e7e;
    --night: #000000;
    --light-text: #ffffff;
  }
  html, body {
    margin: 0;
    width: 1200px;
    height: 1200px;
    overflow: hidden;
    background: var(--backdrop);
  }
  .poster {
    position: absolute;
    left: 219px;
    top: 64px;
    width: 762px;
    height: 1071px;
    background: var(--paper);
    overflow: hidden;
  }
  .stage-wall {
    position: absolute;
    left: 0;
    right: 0;
    top: 350px;
    bottom: 0;
    background:
      radial-gradient(ellipse 50% 40% at 50% 40%, rgba(255,255,255,0.9) 0%, rgba(255,255,255,0) 100%),
      linear-gradient(to bottom,
        var(--paper) 0%,
        #f2f2f2 10%,
        var(--mist) 35%,
        var(--smoke) 62%,
        #262626 82%,
        var(--night) 92%);
  }
  .shadow-figure {
    position: absolute;
    left: 200px;
    top: 345px;
    width: 390px;
    height: 500px;
    border-radius: 45% 45% 30% 30%;
    background: radial-gradient(ellipse 55% 55% at 55% 50%, rgba(110,110,110,0.85) 0%, rgba(126,126,126,0.55) 55%, rgba(126,126,126,0) 100%);
    filter: blur(8px);
  }
  .butterfly {
    position: absolute;
    left: 346px;
    top: 638px;
    width: 188px;
    height: 180px;
    border-radius: 50%;
    background: radial-gradient(ellipse 50% 50% at 55% 50%, #111 0%, #111 55%, rgba(17,17,17,0) 100%);
  }
  .foreground-object {
    position: absolute;
    left: 270px;
    top: 800px;
    width: 233px;
    height: 271px;
    background: linear-gradient(to bottom, #1c1c1c 0%, #0d0d0d 60%, #050505 100%);
    border-radius: 6px 6px 0 0;
  }
  .show-title,
  .artist-name,
  .genre {
    position: absolute;
    left: 0;
    right: 0;
    margin: 0;
    text-align: center;
    font-family: "Bodoni Moda", "Times New Roman", serif;
    font-weight: 400;
    text-transform: uppercase;
    line-height: 1;
    white-space: nowrap;
  }
  .show-title {
    top: 52px;
    padding-left: 22px;
    font-size: 46px;
    letter-spacing: 0.06em;
    color: var(--ink);
  }
  .artist-name {
    top: 124px;
    font-size: 126px;
    font-weight: 500;
    line-height: 110px;
    letter-spacing: 0;
    color: var(--ink);
  }
  .genre {
    top: 975px;
    font-size: 31px;
    letter-spacing: 0.03em;
    color: var(--light-text);
  }
  .event-details {
    position: absolute;
    left: 0;
    right: 0;
    top: 1021px;
    margin: 0;
    text-align: center;
    font-family: "Barlow Semi Condensed", "Arial Narrow", sans-serif;
    font-size: 14px;
    letter-spacing: 0.09em;
    text-transform: uppercase;
    white-space: nowrap;
    color: var(--light-text);
  }
</style>
</head>
<body>
  <main class="poster">
    <div class="stage-wall"></div>
    <div class="shadow-figure" role="img" aria-label="Soft grey shadow of a magician in a hat raising a wand, cast on the spotlit wall"></div>
    <div class="foreground-object" role="img" aria-label="Dark cylindrical object rising from the bottom edge in the foreground"></div>
    <div class="butterfly" role="img" aria-label="Black butterfly silhouette perched on top of the dark object"></div>
    <h2 class="show-title">Die leise Lampe</h2>
    <h1 class="artist-name">Lorenz<br>Habicht</h1>
    <p class="genre">Fesselndes Zauber-Theater</p>
    <p class="event-details">27. bis 30. Mai 2026 - 20:00 - Dachstube St. Gallen Tickets: www.dachstubbe.ch - 071 84 16 72</p>
  </main>
</body>
</html>
```